Double Sided Business Card Design for Pet Services

My mom and I want to start a business for pets. We want to offer dog walking, pet sitting as well as boarding and grooming at our home. For the front of the business card, we want a logo that will capture all of our services. We want the name to be Bigotes, Inc., which means little paws in Spanish. Perhaps, there could be little paws or just a little paw implemented within the word Bigotes. Or we would want a cat and a dog by the word Bigotes. We have a cat and a dog at home, and we would be really happy if they could be a part of the business card. It does not have to be anything crazy. Just an outline of a cat or a dog would be awesome. Please see uploaded file.
As for the back of the card, we would want little paws all over the card or we would want a collar, leash, grooming scissor, dog/cat bowl, bone, fish, or toy to show all of the services that we provide. Along with either the many paws or many pet objects, we would want to add our information, such as name (Lorenza Mireles), telephone numbers (555) 812-3762, e-mail addresses bigotesinc@correomail.net, etc.
We would also want a catch phrase to go on the back of the card, such as "Where every tail counts!" Or "We strive for happy tails." or "Tail-wagging care, every single day!"
As for colors, we would not want that many. We would want perhaps white and blue. We would want soft colors that will stand out and make an impression. The same goes with the text. An elegant text would be nice. Or perhaps a text with bold letters. We are excited to see the results, but we are also excited to see your creative ideas and what you will bring to the table.

Target Market(s)

Pet Owners

Contact Information for Business Card

For the front of the business card, we want a logo that will capture all of our services. We want the name to be Bigotes, Inc., which means little paws in Spanish. Perhaps, there could be little paws or just a little paw implemented within the word Bigotes. Or we would want a cat and a dog by the word Bigotes. We have a cat and a dog at home, and we would be really happy if they could be a part of the business card. It does not have to be anything crazy. Just an outline of a cat or a dog would be awesome. Please see uploaded file.
As for the back of the card, we would want little paws all over the card or we would want a collar, leash, grooming scissor, dog/cat bowl, bone, fish, or toy to show all of the services that we provide. Along with either the many paws or many pet objects, we would want to add our information, such as name, telephone numbers, e-mail addresses, etc. We would also want a catch phrase to go on the back of the card, such as "Where every tail counts!" Or "We strive happy tails." or "Tail-wagging care, every single day!" Or if there is a way to put the catch phrase in the front of the card. We are open to seeing variety.

Logo Text

Bigotes, Inc

Font styles to use
Serif
Script

Colors
ffffff
33a6d7
145ea8

Requirements
Must have
• My project must be a double sided business card.

```html
<!DOCTYPE html>
<html lang="en">
<head>
<meta charset="utf-8">
<title>Bigotes, Inc. – Business Card</title>
<link href="https://fonts.googleapis.com/css2?family=Lato:wght@300;400;700;900&family=Roboto+Condensed:wght@300;400&display=swap" rel="stylesheet">
<style>
  :root{
    --stage:#dcdcde;
    --paper:#ffffff;
    --blue-deep:#145ea8;
    --blue-mid:#2e7fc6;
    --blue-sky:#33a6d7;
    --blue-pale:#a9d2ee;
    --blue-mist:#e6ecf7;
    --text-blue:#1c5fa9;
    --tag-blue:#6fb6e4;
  }
  html,body{margin:0;padding:0;width:1200px;height:1200px;overflow:hidden;background:var(--stage);}
  .canvas{position:relative;width:1200px;height:1200px;}
  .card{position:absolute;left:248px;width:704px;height:447px;background:var(--paper);overflow:hidden;}
  .card--front{top:68px;}
  .card--back{top:618px;}
  .corner{position:absolute;inset:0;width:704px;height:447px;}
  .pattern-band{position:absolute;left:20px;top:250px;width:620px;height:190px;
    background:linear-gradient(160deg,rgba(230,236,247,0) 30%,rgba(214,226,243,.7) 70%,rgba(230,236,247,.3));
    clip-path:polygon(100% 0,100% 60%,60% 100%,0 100%,0 92%);}
  .pattern-edge{position:absolute;right:0;top:30px;width:70px;height:260px;
    background:linear-gradient(180deg,rgba(214,226,243,.2),rgba(214,226,243,.8));}
  .brand-mark{position:absolute;left:306px;top:138px;width:90px;height:92px;border-radius:46px 46px 40px 40px;
    background:linear-gradient(180deg,#d9e6f5,#6f9fd3);}
  .brand-name{position:absolute;left:0;width:704px;top:226px;text-align:center;
    font:900 56px/1 "Lato",sans-serif;color:var(--blue-deep);letter-spacing:2px;margin:0;}
  .brand-tag{position:absolute;left:280px;top:286px;width:212px;text-align:right;margin:0;
    font:300 15px/1 "Lato",sans-serif;color:var(--tag-blue);letter-spacing:.3px;white-space:nowrap;}
  .ghost{position:absolute;left:380px;top:70px;width:280px;height:300px;border-radius:140px 140px 120px 120px;
    background:linear-gradient(180deg,#eef2fa,#e2e9f6);}
  .person{position:absolute;left:66px;top:82px;}
  .holder-name{position:absolute;left:94px;top:128px;margin:0;font:700 34px/1 "Lato",sans-serif;
    font-variant:small-caps;color:var(--text-blue);letter-spacing:.5px;white-space:nowrap;}
  .rule{position:absolute;left:0;top:168px;width:346px;height:3px;background:var(--blue-sky);}
  .contact{position:absolute;left:156px;margin:0;font:400 15px/1 "Lato",sans-serif;color:var(--text-blue);display:flex;align-items:center;gap:2px;white-space:nowrap;}
  .contact--phone{top:200px;font-size:16px;}
  .contact--mail{top:237px;}
  .catchphrase{position:absolute;left:214px;top:406px;margin:0;font:400 16px/1 "Roboto Condensed",sans-serif;color:var(--blue-sky);letter-spacing:.2px;white-space:nowrap;}
  .mini-brand{position:absolute;left:540px;top:346px;width:120px;text-align:center;}
  .mini-brand .dot{display:block;margin:0 auto 4px;width:14px;height:14px;border-radius:50%;background:var(--blue-deep);}
  .mini-brand .name{font:900 22px/1 "Lato",sans-serif;color:var(--blue-deep);letter-spacing:1px;}
  .mini-brand .tag{font:300 7px/1.4 "Lato",sans-serif;color:var(--tag-blue);white-space:nowrap;}
</style>
</head>
<body>
<div class="canvas">

  <section class="card card--front" aria-label="Card front">
    <div class="pattern-band" role="img" aria-label="Faint pattern of pet items: paws, bones, bowls and toys"></div>
    <div class="pattern-edge" role="img" aria-label="Faint pattern of pet items along the edge"></div>
    <svg class="corner" viewBox="0 0 704 447" aria-hidden="true">
      <g class="corner-top-left">
        <polygon points="0,0 440,0 110,80 14,310 0,310" fill="var(--blue-pale)"/>
        <polygon points="0,0 380,0 120,40 14,310 0,310" fill="var(--blue-sky)"/>
        <polygon points="38,55 180,8 90,150 14,310" fill="var(--blue-deep)"/>
        <polygon points="70,45 200,10 110,95 20,300" fill="var(--blue-mid)"/>
        <polygon points="0,0 110,0 20,50 0,310" fill="var(--blue-sky)"/>
      </g>
      <g class="corner-bottom-right" transform="rotate(180 352 223.5)">
        <polygon points="0,0 440,0 110,80 14,310 0,310" fill="var(--blue-pale)"/>
        <polygon points="0,0 380,0 120,40 14,310 0,310" fill="var(--blue-sky)"/>
        <polygon points="38,55 180,8 90,150 14,310" fill="var(--blue-deep)"/>
        <polygon points="70,45 200,10 110,95 20,300" fill="var(--blue-mid)"/>
        <polygon points="0,0 110,0 20,50 0,310" fill="var(--blue-sky)"/>
      </g>
    </svg>
    <div class="brand-mark" role="img" aria-label="Illustration of a dog and a cat together"></div>
    <h1 class="brand-name">BIGOTES</h1>
    <p class="brand-tag">WHERE EVERY TAIL COUNTS!</p>
  </section>

  <section class="card card--back" aria-label="Card back">
    <div class="ghost" role="img" aria-label="Faint large illustration of a dog and a cat"></div>
    <svg class="corner" viewBox="0 0 704 447" aria-hidden="true">
      <g class="corner-top-right" transform="translate(704 0) scale(-1 1)">
        <polygon points="0,0 240,0 40,40 0,170" fill="var(--blue-pale)"/>
        <polygon points="0,0 200,0 30,25 0,170" fill="var(--blue-sky)"/>
        <polygon points="12,20 110,4 40,60 4,165" fill="var(--blue-deep)"/>
        <polygon points="0,0 60,0 8,30 0,170" fill="var(--blue-sky)"/>
      </g>
      <g class="corner-bottom-left" transform="translate(0 447) scale(1 -1) translate(22 0)">
        <polygon points="0,0 180,0 40,30 0,126" fill="var(--blue-pale)"/>
        <polygon points="0,0 150,0 30,18 0,126" fill="var(--blue-sky)"/>
        <polygon points="10,15 80,4 30,45 4,122" fill="var(--blue-deep)"/>
        <polygon points="0,0 50,0 6,22 0,126" fill="var(--blue-sky)"/>
      </g>
    </svg>

    <svg class="person" width="90" height="50" viewBox="0 0 90 50" aria-hidden="true">
      <circle cx="42" cy="12" r="10" fill="var(--blue-deep)"/>
      <path d="M24 44 Q26 24 42 24 Q58 24 60 44 Z" fill="var(--blue-deep)"/>
      <path d="M0 50 Q40 30 90 48" stroke="var(--blue-deep)" stroke-width="2" fill="none"/>
    </svg>
    <h2 class="holder-name">Lorenza Mireles</h2>
    <div class="rule"></div>

    <p class="contact contact--phone">
      <svg width="28" height="18" viewBox="0 0 26 18" aria-hidden="true">
        <path d="M6 2 Q2 3 4 8 Q7 13 12 14 Q16 14 15 11 L12 9 L10 11 Q7 9 6 6 L8 4 Z" fill="var(--blue-deep)"/>
        <path d="M0 17 Q10 12 24 16" stroke="var(--blue-deep)" stroke-width="1.5" fill="none"/>
      </svg>(555) 812-3762
    </p>
    <p class="contact contact--mail">
      <svg width="28" height="18" viewBox="0 0 26 18" aria-hidden="true">
        <rect x="7" y="1" width="16" height="11" fill="var(--blue-deep)"/>
        <path d="M7 1 L15 8 L23 1" stroke="#fff" stroke-width="1.2" fill="none"/>
        <path d="M0 17 Q10 12 24 16" stroke="var(--blue-deep)" stroke-width="1.5" fill="none"/>
      </svg>bigotesinc@correomail.net
    </p>

    <p class="catchphrase">TAIL-WAGGING CARE, EVERY SINGLE DAY!</p>

    <div class="mini-brand">
      <span class="dot"></span>
      <div class="name">BIGOTES</div>
      <div class="tag">WHERE EVERY TAIL COUNTS!</div>
    </div>
  </section>

</div>
</body>
</html>
```